Law Firm Investment Immigration Brochure

I'm looking to have a brochure designed for my law firm. The brochure will be about investment immigration and will be designed to attract potential immigrations.
As this program is geared towards wealthier clients, I will need the winning brochure design to be classy.
The overall theme of my brochure should be to look simple, elegant, smart and professional.
I would like the delivery of the brochure in high-res PSD and AI formats in CS1 and CS3, which can be resized later to any resolution possible (print ready included). I will then own the rights to the content once the work has been paid for. I will need multiple formats - .psd (CS1 and CS3), .ai (CS1 and CS3), .jpg, and .gif.
I have included a copy of my logo design so please design the brochure accordingly.
The name of my law firm is "Law Offices of Marcel Dovrane".
Thanks in advance.
Updates
Even though my brochure is 1 page, I will be folding it twice, so that it looks like an "N". The side that clients will see first will act as the cover page. Therefore, on it, I would like you to include my logo design and then my office address (which I will supply to you later). My cover page would take up the right 1/3 of this design you will submit. Therefore, please submit a design which would take up the left 2/3 of the page, and then design a cover page that will take up the right 1/3 of the page. Just so you know, my brochure will be 2-sided, so please show me what both sides will look like. The back side of the brochure will have all written content, and no cover page. Therefore, please design the whole back side of the brochure as one, instead of the front side, which is split 2/3 and 1/3. Thank you in advance, Marc

```html
<!DOCTYPE html>
<html lang="en">
<head>
<meta charset="utf-8">
<title>Investment Immigration Brochure – Law Offices of Marcel Dovrane</title>
<link rel="stylesheet" href="https://fonts.googleapis.com/css2?family=Cinzel:wght@600;700&family=Hind:wght@400;600&family=Arimo:wght@400;700&display=swap">
<style>
  :root {
    --royal: #0c1cb2;
    --royal-deep: #08138c;
    --ink: #2b2b2b;
    --paper: #ffffff;
    --mist: #e6e9ec;
    --steel: #9aa4ad;
    --frame: rgba(255,255,255,0.55);
    --frame-soft: rgba(120,130,150,0.14);
  }
  * { margin: 0; padding: 0; box-sizing: border-box; }
  html, body { width: 800px; height: 1200px; overflow: hidden; background: var(--paper); }
  body { position: relative; font-family: "Hind", Arial, sans-serif; color: var(--ink); }

  .sheet { position: absolute; left: 29px; width: 749px; box-shadow: 2px 3px 5px rgba(0,0,0,0.35); overflow: hidden; background: var(--paper); }
  .sheet--front { top: 21px; height: 576px; }
  .sheet--back { top: 611px; height: 579px; }

  .cell { position: absolute; overflow: hidden; }
  .col-1 { left: 0; width: 250px; }
  .col-2 { left: 250px; width: 250px; }
  .col-3 { left: 500px; width: 249px; }

  .blue { background: var(--royal); color: var(--paper); }
  .mist { background: linear-gradient(100deg, #dfe3e7 0%, #f7f8f9 70%, #ffffff 100%); }
  .steel { background: linear-gradient(115deg, #f4f5f6 0%, #d4d9de 45%, #9aa4ad 100%); }
  .base-band { position: absolute; left: 0; right: 0; bottom: 0; height: 27px; background: var(--royal); }

  .outline-frame { position: absolute; border: 9px solid var(--frame-soft); border-radius: 16px; }
  .blue .outline-frame { border-color: rgba(255,255,255,0.06); }

  .heading {
    font-family: "Cinzel", "Times New Roman", serif; font-weight: 700;
    font-size: 18px; letter-spacing: 0.6px; text-align: center; line-height: 1;
  }
  .blue .heading { color: var(--paper); }
  .mist .heading, .steel .heading { color: #1d1d1d; }
  .copy { font-size: 8.6px; line-height: 15px; margin: 0 auto; width: 172px; }
  .copy p + p { margin-top: 4px; }
  .subhead { font-weight: 600; text-align: center; font-size: 8.6px; letter-spacing: 0.4px; margin: 8px 0 6px; }

  .block { position: absolute; left: 0; right: 0; }
  .block .heading { margin-bottom: 10px; }

  .quote { font-family: "Arimo", Arial, sans-serif; font-size: 8.4px; line-height: 10.5px; color: var(--royal); text-align: center; padding: 0 18px; }
  .quote .mark { font-size: 12px; font-weight: 700; }
  .quote cite { display: block; font-style: normal; font-weight: 700; }

  .photo { position: absolute; }

  .brand { position: absolute; left: 14px; top: 24px; display: flex; align-items: center; gap: 10px; }
  .brand-square { width: 30px; height: 30px; background: var(--royal); flex: none; }
  .brand-name { font-family: "Hind", Arial, sans-serif; font-weight: 600; font-size: 12.5px; line-height: 14px; color: var(--royal); text-transform: uppercase; letter-spacing: 0.5px; }

  .contact { text-align: center; font-size: 9.2px; line-height: 17.5px; }
  .contact .row { display: flex; justify-content: center; gap: 14px; }

  .cover-title { position: absolute; left: 0; right: 0; top: 265px; text-align: center; font-family: "Cinzel", "Times New Roman", serif; font-weight: 700; font-size: 21px; line-height: 24px; letter-spacing: 1.2px; color: var(--royal); }
  .cover-tagline { position: absolute; left: 88px; width: 120px; top: 421px; text-align: center; font-family: "Arimo", Arial, sans-serif; font-weight: 700; font-size: 11px; line-height: 11.5px; letter-spacing: 1px; color: var(--royal); text-transform: uppercase; }

  .quote-frame { position: absolute; left: 48px; top: 200px; width: 166px; height: 126px; border: 7px solid var(--paper); border-radius: 16px; }
  .quote--light { color: var(--paper); padding: 0; }
</style>
</head>
<body>

<!-- Front side: inner spread (left two thirds) and cover (right third) -->
<section class="sheet sheet--front" aria-label="Brochure front side">
  <div class="cell col-1 blue" style="top:0;height:189px;">
    <div class="outline-frame" style="left:-20px;top:20px;width:90px;height:110px;"></div>
    <div class="block" style="top:30px;">
      <h2 class="heading">What we do</h2>
      <div class="copy"><p>Batman sacrificed the elephants. One mat mostly lamely towed two aardvarks, because poisons ran away. One subway tastes five trailers, even though Mark laughed, but almost progressive wart hogs sacrificed two quixotic aardvarks, however Paul kisses extremely bourgeois bureaux.</p></div>
    </div>
  </div>
  <div class="cell col-2 blue" style="top:0;height:189px;">
    <div class="outline-frame" style="left:160px;top:-20px;width:90px;height:100px;"></div>
    <div class="block" style="top:30px;">
      <h2 class="heading">The Team</h2>
      <div class="copy"><p>Batman sacrificed the elephants. One mat mostly lamely towed two aardvarks, because poisons ran away. One subway tastes five trailers, even though Mark laughed, but almost progressive wart hogs sacrificed two quixotic aardvarks, however Paul kisses extremely bourgeois bureaux.</p></div>
    </div>
  </div>
  <div class="cell col-3 photo" role="img" aria-label="Photograph of passports and travel tickets" style="top:0;height:189px;background:linear-gradient(135deg,#3c4f8a 0%,#14204f 55%,#0b1433 100%);"></div>

  <div class="cell col-1" style="top:189px;height:80px;background:var(--paper);">
    <blockquote class="quote" style="margin-top:4px;"><span class="mark">“</span>Two extremely angst -ridden bureaux tastes umpteen schizophrenic cats. Wart hogs ran away, and the almost purple bureau sacr ificed five poisons.<cite>Lena Harcourt</cite><cite>Company Name</cite></blockquote>
  </div>
  <div class="cell col-2 photo" role="img" aria-label="Photograph of travellers at an airport check-in hall" style="top:189px;height:80px;background:linear-gradient(180deg,#c9ccce 0%,#7d8184 45%,#2e3033 100%);"></div>
  <div class="cell col-3" style="top:189px;height:80px;background:var(--paper);">
    <div class="brand"><span class="brand-square"></span><span class="brand-name">Law Offices of<br>Marcel Dovrane</span></div>
  </div>

  <div class="cell col-1 mist" style="top:269px;height:280px;">
    <div class="outline-frame" style="left:-30px;top:40px;width:110px;height:130px;"></div>
    <div class="outline-frame" style="left:140px;top:150px;width:80px;height:140px;"></div>
    <div class="block" style="top:20px;">
      <h2 class="heading">Why Use Us?</h2>
      <div class="copy">
        <p>Umpteen bourgeois Macintoshes grew up, and Phil comfortablart hog. Subways boy auctioned off one wart hog. Subways bought umpteen purple dogs.</p>
        <p>Umpteen Macintoshes laughed quickly. The putrid orifice marriesart hog. Subways bo five bourgeois televisions, although one f one wart hog. Subways bought umpteen purple dogs.</p>
        <p class="subhead">SUB HEAD ONE</p>
        <p>One poison tickled the silly elephant.</p>
        <p>Umpteen Macintoshes laughed quickly. The putrid orifice marart hog. Subways bories five bourgeois televisions, although one Klingon Mercury.</p>
      </div>
    </div>
  </div>
  <div class="cell col-2 mist" style="top:269px;height:280px;background:linear-gradient(100deg,#f3f4f5 0%,#ffffff 100%);">
    <div class="outline-frame" style="left:100px;top:20px;width:80px;height:90px;"></div>
    <div class="outline-frame" style="left:150px;top:40px;width:90px;height:240px;"></div>
    <div class="photo" role="img" aria-label="Photograph of a self-service check-in screen" style="left:34px;top:8px;width:80px;height:80px;border-radius:6px;background:linear-gradient(140deg,#4a5a4a 0%,#1b221d 60%,#0c0f0d 100%);"></div>
    <div class="block" style="top:108px;">
      <h2 class="heading" style="margin-bottom:8px;">Contact Us</h2>
      <div class="contact">
        <div>To schedule your complimentary</div>
        <div>consultancy meeting, please contact</div>
        <div>Marcel Dovrane • Address line one • Address name</div>
        <div>City name • Zipcode</div>
        <div>www.marceldovrane.com • info@marceldovrane</div>
        <div class="row"><span>Office one name</span><span>: +345 610 228</span></div>
        <div class="row"><span>Office two name</span><span>: +345 610 228</span></div>
      </div>
    </div>
  </div>
  <div class="cell col-3 steel" style="top:269px;height:280px;background:transparent;"></div>
  <div class="cell col-3 steel" style="top:269px;height:280px;">
    <div class="outline-frame" style="left:75px;top:75px;width:100px;height:110px;border-color:var(--frame);"></div>
    <div class="outline-frame" style="left:0px;top:150px;width:100px;height:95px;border-color:var(--frame);"></div>
  </div>
  <h1 class="cover-title" style="left:500px;width:249px;">Investment<br>Immigration</h1>
  <p class="cover-tagline" style="left:588px;">Providing you that special link</p>
  <div class="base-band"></div>
</section>

<!-- Back side: full content spread -->
<section class="sheet sheet--back" aria-label="Brochure back side">
  <div class="cell col-1 blue" style="top:0;height:164px;">
    <div class="outline-frame" style="left:-20px;top:10px;width:100px;height:120px;"></div>
    <div class="block" style="top:31px;">
      <h2 class="heading">Headline 4</h2>
      <div class="copy"><p>Batman sacrificed the elephants. One mat mostly lamely towed two aardvarks, because poisons ran away. One subway tastes five trailers, even though Mark laughed, but almost progressive wart hogs sacrificed two quixotic aardvarks, however Paul kisses extremely bourgeois bureaux.</p></div>
    </div>
  </div>
  <div class="cell col-2 blue" style="top:0;height:551px;">
    <div class="block" style="top:31px;">
      <h2 class="heading">Headline SIX</h2>
      <div class="copy"><p>Batman sacrificed the elephants. One mat mostly lamely towed two aardvarks, because poisons ran away. One subway tastes five trailers, even though Mark laughed, but almost progressive wart hogs sacrificed two quixotic aardvarks, however Paul kisses extremely bourgeois bureaux.</p></div>
    </div>
    <div class="quote-frame"></div>
    <div class="photo" role="img" aria-label="Portrait photograph of a smiling client" style="left:28px;top:160px;width:80px;height:90px;border:6px solid var(--paper);border-radius:14px;background:linear-gradient(150deg,#f1ece6 0%,#cdb8a6 55%,#6e5b50 100%);"></div>
    <blockquote class="quote quote--light" style="position:absolute;left:58px;width:146px;top:254px;"><span class="mark">“</span>Two extremely angst -ridden bureaux tastes umpt een sch izophr enic cats. Wart hogs ran away, and the almost purple bureau sacr ificed five poisons.<cite style="margin-top:3px;">Lena Harcourt Company Name</cite></blockquote>
    <div class="block" style="top:363px;">
      <h2 class="heading" style="margin-bottom:8px;">Headline seven</h2>
      <div class="copy"><p>Batman sacrificed the elephants. One mat mostly lamely towedMark laughed, but almost progressive wart hogs Mark laughed, but almost progressive wart hogs two aardvarks, because poisons ran away. One subway tastes five trailers, even though Mark laughed, but almost progressive wart hogs sacrificed two quixotic aardvarks, however Paul kisses extremely bourgeois bureaux.</p></div>
    </div>
  </div>
  <div class="cell col-3 blue" style="top:0;height:164px;">
    <div class="outline-frame" style="left:150px;top:20px;width:110px;height:120px;"></div>
    <div class="block" style="top:31px;">
      <h2 class="heading">Headline EIGHT</h2>
      <div class="copy"><p>Batman sacrificed the elephants. One mat mostly lamely towed two aardvarks, because poisons ran away. One subway tastes five trailers, even though Mark laughed, but almost progressive wart hogs sacrificed two quixotic aardvarks, however Paul kisses extremely bourgeois bureaux.</p></div>
    </div>
  </div>

  <div class="cell col-1" style="top:164px;height:108px;background:var(--paper);">
    <blockquote class="quote" style="margin-top:14px;"><span class="mark">“</span>Two extremely angst -ridden bureaux tastes umpteen schizophrenic cats. Wart hogs ran away, and the almost purple bureau sacr ificed five poisons.<cite>Lena Harcourt</cite><cite>Company Name</cite></blockquote>
  </div>
  <div class="cell col-3" style="top:164px;height:108px;background:var(--paper);">
    <blockquote class="quote" style="margin-top:14px;"><span class="mark">“</span>Two extremely angst -ridden bureaux tastes umpteen schizophrenic cats. Wart hogs ran away, and the almost purple bureau sacr ificed five poisons.<cite>Owen Pell</cite><cite>Company Name</cite></blockquote>
  </div>

  <div class="cell col-1 mist" style="top:272px;height:279px;">
    <div class="outline-frame" style="left:-30px;top:40px;width:110px;height:130px;"></div>
    <div class="outline-frame" style="left:140px;top:150px;width:80px;height:140px;"></div>
    <div class="block" style="top:14px;">
      <h2 class="heading">Headline five?</h2>
      <div class="copy">
        <p>Umpteen bourgeois Macintoshes grew up, and Phil comfortablart hog. Subways boy auctioned off one wart hog. Subways bought umpteen purple dogs.</p>
        <p>Umpteen Macintoshes laughed quickly. The putrid orifice marriesart hog. Subways bo five bourgeois televisions, although one f one wart hog. Subways bought umpteen purple dogs.</p>
        <p class="subhead">SUB HEAD ONE</p>
        <p>One poison tickled the silly elephant.</p>
        <p>Umpteen Macintoshes laughed quickly. The putrid orifice marart hog. Subways bories five bourgeois televisions, although one Klingon Mercury.</p>
      </div>
    </div>
  </div>
  <div class="cell col-3 steel" style="top:272px;height:279px;">
    <div class="outline-frame" style="left:100px;top:20px;width:110px;height:130px;border-color:var(--frame);"></div>
    <div class="outline-frame" style="left:60px;top:120px;width:130px;height:170px;border-color:var(--frame);"></div>
    <div class="block" style="top:14px;">
      <h2 class="heading">Headline Nine</h2>
      <div class="copy">
        <p>Umpteen bourgeois Macintoshes grew up, and Phil comfortablart hog. Subways boy auctioned off one wart hog. Subways bought umpteen purple dogs.</p>
        <p>Umpteen Macintoshes laughed quickly. The putrid orifice marriesart hog. Subways bo five bourgeois televisions, although one f one wart hog. Subways bought umpteen purple dogs.</p>
        <p class="subhead">SUB HEAD ONE</p>
        <p>One poison tickled the silly elephant.</p>
        <p>Umpteen Macintoshes laughed quickly. The putrid orifice marart hog. Subways bories five bourgeois televisions, although one Klingon Mercury.</p>
      </div>
    </div>
  </div>
  <div class="base-band" style="height:28px;"></div>
</section>

</body>
</html>
```